Business Card Design Project

Business Card
We are rebranding with a new logo
Industry/Entity Type
Business
Contact Information for Business Card
Dennis Marlow +61 427581962 dennis@qovo.com.au P.O. Box 872 Kelvindale QLD 4309
Requirements
Must have
- Logo

```html
<!DOCTYPE html>
<html lang="en">
<head>
<meta charset="utf-8">
<title>Qovo International – Business Card</title>
<link href="https://fonts.googleapis.com/css2?family=Poppins:wght@300;500;700&family=Righteous&display=swap" rel="stylesheet">
<style>
  :root {
    --page: #ffffff;
    --card: #120d15;
    --divider: #1f2a2b;
    --orange: #f47f20;
    --blue: #1aa1dc;
    --white: #ffffff;
    --muted: #c8c8da;
  }
  * { margin: 0; padding: 0; box-sizing: border-box; }
  html, body {
    width: 1200px;
    height: 1000px;
    overflow: hidden;
    background: var(--page);
  }
  .card {
    position: absolute;
    left: 137px;
    top: 201px;
    width: 927px;
    height: 598px;
    background: var(--card);
    font-family: "Poppins", sans-serif;
  }
  .brand {
    position: absolute;
    left: 40px;
    top: 268px;
    width: 270px;
    display: flex;
    align-items: center;
    justify-content: center;
    gap: 12px;
    color: var(--orange);
    font-weight: 500;
    font-size: 25px;
    letter-spacing: 1px;
    white-space: nowrap;
  }
  .brand-dot {
    width: 16px;
    height: 16px;
    border-radius: 50%;
    background: var(--orange);
    flex: none;
  }
  .divider {
    position: absolute;
    left: 356px;
    top: 161px;
    width: 2px;
    height: 265px;
    background: var(--divider);
  }
  .details {
    position: absolute;
    left: 420px;
    top: 175px;
  }
  .person-name {
    font-family: "Righteous", sans-serif;
    font-size: 46px;
    line-height: 1;
    letter-spacing: 0.5px;
    white-space: nowrap;
  }
  .person-name .first { color: var(--orange); }
  .person-name .last { color: var(--blue); }
  .contact-list {
    list-style: none;
    margin-top: 43px;
  }
  .contact-item {
    display: flex;
    align-items: center;
    height: 30px;
    margin-bottom: 25px;
    color: var(--muted);
    font-weight: 300;
    font-size: 22px;
    white-space: nowrap;
  }
  .contact-item.phone {
    color: var(--white);
    font-weight: 700;
    font-size: 24px;
  }
  .contact-icon {
    width: 24px;
    height: 28px;
    margin-right: 26px;
    flex: none;
  }
</style>
</head>
<body>
  <main class="card">
    <div class="brand">
      <span class="brand-dot"></span>
      <span class="brand-name">Qovo International</span>
    </div>

    <div class="divider"></div>

    <section class="details">
      <h1 class="person-name"><span class="first">Dennis</span> <span class="last">Marlow</span></h1>
      <ul class="contact-list">
        <li class="contact-item phone">
          <svg class="contact-icon" viewBox="0 0 24 28" fill="none" stroke="#ffffff" stroke-width="1.4">
            <rect x="5" y="1.5" width="14" height="25" rx="2.5"/>
            <line x1="5" y1="21" x2="19" y2="21"/>
          </svg>
          +61 427581962
        </li>
        <li class="contact-item email">
          <svg class="contact-icon" viewBox="0 0 24 28" fill="none" stroke="#ffffff" stroke-width="1.3">
            <rect x="1.5" y="8" width="21" height="13" rx="1"/>
            <polyline points="1.5,8 12,16 22.5,8"/>
            <line x1="1.5" y1="21" x2="9" y2="14"/>
            <line x1="22.5" y1="21" x2="15" y2="14"/>
          </svg>
          dennis@qovo.com.au
        </li>
        <li class="contact-item address">
          <svg class="contact-icon" viewBox="0 0 24 28" fill="none" stroke="#ffffff" stroke-width="1.4">
            <path d="M12 26 C6 18 3 14 3 10 A9 9 0 0 1 21 10 C21 14 18 18 12 26 Z"/>
            <circle cx="12" cy="10" r="3.5"/>
          </svg>
          P.O. Box 872 Kelvindale QLD 4309
        </li>
      </ul>
    </section>
  </main>
</body>
</html>
```